AMAZING WEBSITE DESIGN NEEDED FOR MAID / CLEANING SERVICE

NOTE: This is Website Design Only - No coding required

Please submit your designs ASAP as we want to pick a winner and get started!

Hey,

We are looking for a new amazing website design for a maid or cleaning service.

They have a horrible website that we want turned into a masterpiece.

As you will see on their current site:

http://tidyharborco.examplehost.net/

They have a lot of stuff, very disorganized, and need help.

Here is what we need:

Colors: Same as current site, Orange, Gray, Black

Menu: Horizontal with same Menu items

Need a spot for a video on the homepage

Want content to be structured in a great format that is easy to read.

Want to highlight commercial and residential on the website homepage.

Also want a spot for customer testimonials

We want the site clean, professional, fresh and modern.

Please help by matching the logo design.

I look forward to your designs!
Updates

Hi All! Really appreciate your efforts and designs. I will be meeting with our client on Monday and will then be able to provide feedback after our meeting. If you have other ideas, please submit them. The more I can show him the better! Thanks!

Target Market(s)

The target market is residential home owners as well as commercial businesses who need cleaning on a regular basis.

This company cleans homes and offices for individuals.

Industry/Entity Type

Residential

Font styles to use
Sans Serif

Requirements
Must have
• Must match logo colors
Must have spot for video
Must have a clean look
Must have a bold look
Nice to have
• Highly visual
Should not have
• clutter
messy design
hard to read

```html
<!DOCTYPE html>
<html lang="en">
<head>
<meta charset="utf-8">
<title>Tidy Harbor – Quality Commercial &amp; Residential Cleaning</title>
<link href="https://fonts.googleapis.com/css2?family=Ubuntu:wght@400;500;700&family=Arimo:ital,wght@0,400;0,700;1,400&display=swap" rel="stylesheet">
<style>
:root{
  --orange:#e57d1c;
  --orange-dark:#c8661a;
  --header-gray:#e9e9e9;
  --ink:#4a4a4a;
  --muted:#777;
  --rule:#e2e2e2;
  --footer:#3b3c3e;
  --footer-base:#2b2b2c;
  --white:#fff;
}
*{margin:0;padding:0;box-sizing:border-box}
html,body{width:982px;height:1200px;overflow:hidden;background:var(--white)}
body{position:relative;font-family:"Arimo",Arial,sans-serif;color:var(--ink)}
.abs{position:absolute}
.top-strip{left:0;top:0;width:982px;height:8px;background:var(--orange)}
.site-header{left:0;top:8px;width:982px;height:108px;background:var(--header-gray)}
.brand{left:100px;top:48px;display:flex;align-items:center;gap:8px}
.brand-mark{width:22px;height:22px;background:var(--orange)}
.brand-name{font-family:"Ubuntu",sans-serif;font-weight:700;font-size:27px;color:var(--orange);letter-spacing:.5px}
.brand-tagline{left:134px;top:97px;font-family:"Arimo",sans-serif;font-size:10px;color:#666}
.social{left:694px;top:41px;display:flex;align-items:center;gap:5px;font-size:10px;color:#444}
.social span{margin-right:3px}
.social i{display:block;width:20px;height:20px;border-radius:4px}
.s1{background:#3aa7e2}.s2{background:#cc2b26}.s3{background:#3b5a9a}.s4{background:#1c7bb8}
.search{left:736px;top:78px;width:148px;height:18px;border:2px solid #cfcfcf;border-radius:9px;background:#f4f4f4;font-size:10px;color:#555;padding:1px 0 0 15px}
.search svg{position:absolute;right:4px;top:0}
.nav-band{left:0;top:116px;width:982px;height:44px}
.main-nav{left:100px;top:122px;display:flex;height:32px;align-items:center}
.main-nav a{color:var(--white);text-decoration:none;font-size:12.3px;padding:4px 7px;border-right:1px solid rgba(0,0,0,.12);border-left:1px solid rgba(255,255,255,.18);line-height:17px}
.main-nav a:first-child{border-left:none}
.main-nav a:last-child{border-right:none}
.main-nav a.active{background:#555;border:1px solid #ddd;margin:0 2px}
.hero{left:0;top:160px;width:982px;height:381px;background:linear-gradient(180deg,#f3f3f3 0%,#d8d6d3 40%,#a9704a 62%,#6b4430 100%)}
.intro-title{left:0;top:563px;width:982px;text-align:center;font-family:"Ubuntu",sans-serif;font-size:20px;letter-spacing:1.2px;color:#555}
.intro-title em{font-style:normal;color:var(--orange)}
.intro-copy{left:0;top:614px;width:982px;text-align:center;font-size:11.5px;line-height:16.5px;color:#777}
.rule{height:2px;background:linear-gradient(90deg,transparent,var(--rule) 20%,var(--rule) 80%,transparent)}
.col-sep{width:1px;height:213px;background:var(--rule);top:716px}
.feature h2{font-family:"Ubuntu",sans-serif;font-weight:400;font-size:17px;letter-spacing:.8px;color:#444;margin:0 0 11px 3px}
.feature .thumb{width:239px;height:97px;position:relative;box-shadow:0 6px 5px -5px rgba(0,0,0,.25)}
.feature p{font-family:"Ubuntu",sans-serif;font-size:11px;line-height:16.4px;color:#808080;margin-top:17px;width:245px}
.play{position:absolute;left:92px;top:30px;width:42px;height:40px;border-radius:8px;background:#111;border:2px solid #444}
.play:after{content:"";position:absolute;left:15px;top:10px;border-left:14px solid #fff;border-top:9px solid transparent;border-bottom:9px solid transparent}
.site-footer{left:0;top:987px;width:982px;height:185px;background:var(--footer)}
.footer-base{left:0;top:1172px;width:982px;height:28px;background:var(--footer-base)}
.footer-head{font-family:"Ubuntu",sans-serif;font-size:16.5px;color:var(--white);letter-spacing:.8px;top:1009px}
.links{list-style:none;font-size:10.3px;color:var(--white);top:1050px}
.links li{height:19.6px;position:relative;padding-left:14px}
.links li:before{content:"";position:absolute;left:2px;top:4px;width:5px;height:5px;border-radius:50%;background:#ddd}
.quote-box{left:393px;top:1052px;width:211px;height:100px;border:1px solid #ccc;font-style:italic;font-size:10px;line-height:16.4px;color:var(--white);text-align:center;padding:12px 6px 0}
.quote-avatar{left:462px;top:1129px;width:54px;height:54px;border-radius:50%;background:linear-gradient(180deg,#f1ece6,#c9a77e 60%,#2f2f32);border:2px solid #fff}
.quote-name{left:518px;top:1134px;font-style:italic;font-size:11.5px;color:var(--white)}
.contact{left:650px;top:1052px;font-size:10.3px;line-height:16.4px;color:var(--white)}
.contact .row{display:flex;gap:10px}
.contact .ic{width:9px;flex:none;padding-top:3px}
.copyright{left:117px;top:1179px;font-size:10.3px;color:var(--white)}
</style>
</head>
<body>
<div class="abs top-strip"></div>
<header class="abs site-header"></header>
<div class="abs brand"><i class="brand-mark"></i><span class="brand-name">TIDY HARBOR</span></div>
<div class="abs brand-tagline">Quality Commercial &amp; Residential Cleaning</div>

<div class="abs social"><span>Socialize with us :-</span><i class="s1"></i><i class="s2"></i><i class="s3"></i><i class="s4"></i></div>
<div class="abs search">...... Search here ......
  <svg width="20" height="16" viewBox="0 0 20 16"><circle cx="8" cy="7" r="5" fill="none" stroke="#333" stroke-width="2"/><line x1="12" y1="10.5" x2="18" y2="15" stroke="#333" stroke-width="3" stroke-linecap="round"/></svg>
</div>

<svg class="abs nav-band" width="982" height="44" viewBox="0 0 982 44">
  <path d="M0 0 H982 V4 H912 Q892 4 886 20 Q880 40 860 40 H122 Q102 40 96 20 Q90 4 70 4 H0 Z" fill="var(--orange)"/>
  <path d="M122 40 H860" stroke="#b45a14" stroke-width="2"/>
</svg>
<nav class="abs main-nav">
  <a href="#">Home</a><a href="#" class="active">Our Services</a><a href="#">Our Employees</a><a href="#">Why Choose Us ?</a><a href="#">Testimonials</a><a href="#">Special Offers</a><a href="#">About Us</a><a href="#">Contact Us</a><a href="#">Request a Bid</a>
</nav>

<div class="abs hero" role="img" aria-label="Photo of a cleaner in a blue apron wiping a conference room table"></div>

<h1 class="abs intro-title" style="font-weight:400">Never deal with an unresponsive franchise – <em>Deal with the owner!</em></h1>
<p class="abs intro-copy">Lorem ipsum dolor sit amet, consectetur adipisicing elit, sed do eiusmod tempor incididunt ut labore et dolore magna aliqua.<br>Ut enim ad minim veniam, quis nostrud exercitation ullamco laboris nisi ut aliquip ex ea commodo consequat.</p>

<div class="abs rule" style="left:90px;top:676px;width:800px"></div>

<section class="abs feature" style="left:96px;top:716px">
  <h2>About Our Company</h2>
  <div class="thumb" role="img" aria-label="Photo of a cleaner vacuuming a ceiling vent" style="background:linear-gradient(135deg,#e8e8e8,#9a9a9a 55%,#2a55a5 80%,#5a5a5a)"></div>
  <p>Donec consectetur libero tortor condimentum egestas viverra sed. Dolor sit amet consectetur adipiscing elit, Sed do euismod tempor incidunt magna aliqua..</p>
</section>
<div class="abs col-sep" style="left:352px"></div>
<section class="abs feature" style="left:372px;top:716px">
  <h2>Why Choose Us ?</h2>
  <div class="thumb" role="img" aria-label="Video: cleaner polishing a chandelier" style="background:linear-gradient(90deg,#3a2a18,#b88b3a 40%,#e3b03a 70%,#2450a0)"><span class="play"></span></div>
  <p>Donec consectetur libero tortor condimentum egestas viverra sed. Dolor sit amet consectetur adipiscing elit, Sed do euismod tempor incidunt magna aliqua..</p>
</section>
<div class="abs col-sep" style="left:628px"></div>
<section class="abs feature" style="left:648px;top:716px">
  <h2>Request a Bid</h2>
  <div class="thumb" role="img" aria-label="Photo of a clean kitchen with wooden cabinets" style="background:linear-gradient(90deg,#e9e9e9,#b9753e 35%,#d9c9ad 65%,#a9703d)"></div>
  <p>Donec consectetur libero tortor condimentum egestas viverra sed. Dolor sit amet consectetur adipiscing elit, Sed do euismod tempor incidunt magna aliqua..</p>
</section>

<div class="abs rule" style="left:90px;top:961px;width:800px"></div>

<footer class="abs site-footer"></footer>
<h3 class="abs footer-head" style="left:137px;font-weight:400">Our links</h3>
<h3 class="abs footer-head" style="left:393px;font-weight:400">Testimonials</h3>
<h3 class="abs footer-head" style="left:650px;font-weight:400">Contact us</h3>

<ul class="abs links" style="left:138px">
  <li>Home</li><li>Our Services</li><li>Our Employees</li><li>Why Choose Us ?</li><li>Testimonials</li><li>Special Offers</li>
</ul>
<ul class="abs links" style="left:257px">
  <li>About Us</li><li>Contact Us</li><li>Request a Bid</li>
</ul>

<blockquote class="abs quote-box">“This is a company designed around the customer! We will make sure that you are accomodated in every way possible. ”</blockquote>
<div class="abs quote-avatar" role="img" aria-label="Customer portrait"></div>
<div class="abs quote-name">Dana 29 Years</div>

<address class="abs contact" style="font-style:normal">
  <div class="row"><span class="ic"><svg width="7" height="10" viewBox="0 0 7 10"><path d="M3.5 0A3.5 3.5 0 0 0 0 3.5C0 6 3.5 10 3.5 10S7 6 7 3.5A3.5 3.5 0 0 0 3.5 0Z" fill="#fff"/><circle cx="3.5" cy="3.5" r="1.3" fill="#3b3c3e"/></svg></span><span>4120 Lantern Cove Road Suite 310<br>Marlow Bay | Oregon | 97001</span></div>
  <div class="row"><span class="ic"><svg width="9" height="9" viewBox="0 0 9 9"><path d="M1 0.5L3 0.5 3.8 2.6 2.6 3.6Q3.6 5.4 5.4 6.4L6.4 5.2 8.5 6V8Q8.5 8.8 7.5 8.8 0.2 8 0.2 1.5 0.2 0.5 1 0.5Z" fill="#fff"/></svg></span><span>(555) 014-2200 Office<br>(555) 014-2299 Fax</span></div>
  <div class="row"><span class="ic"><svg width="9" height="7" viewBox="0 0 9 7"><rect width="9" height="7" fill="#fff"/><path d="M0 0L4.5 4 9 0" fill="none" stroke="#3b3c3e"/></svg></span><span>hello@tidyharbor.example</span></div>
</address>

<div class="abs footer-base"></div>
<div class="abs copyright">Copyright © 2014 Tidy Harbor.com . All Right Reserved</div>
</body>
</html>
```